Product flyer with pricing

We manufacture iconic and luxury vending trailers. for our first trailer we need a flyer created to give to prospective clients with base pricing. I am uploading an example along with graphic files.

```html
<!DOCTYPE html>
<html lang="en">
<head>
<meta charset="utf-8">
<title>The Meadow Barn Mini – Flyer</title>
<link rel="stylesheet" href="https://fonts.googleapis.com/css2?family=Oswald:wght@500;600;700&family=Roboto:ital,wght@0,400;0,500;0,700;0,900;1,400&display=swap">
<style>
  :root{
    --stage:#2e2e2e;
    --orange:#e2a22c;
    --green:#5aa646;
    --green-deep:#4a9538;
    --sky-top:#4f8fd6;
    --sky-mid:#8fbce8;
    --sky-low:#cfe3f5;
    --ground:#c6c7c9;
    --card:#f2f3f5;
    --ink:#1f1f1f;
    --white:#ffffff;
  }
  *{box-sizing:border-box;margin:0;padding:0}
  html,body{width:1200px;height:1200px;overflow:hidden;background:var(--stage)}
  .flyer{position:absolute;left:226px;top:71px;width:748px;height:1058px;background:var(--white);overflow:hidden;font-family:"Roboto",Arial,sans-serif;color:var(--ink)}
  .header{position:absolute;left:0;top:0;width:748px;height:134px}
  .header svg{position:absolute;inset:0}
  .brand{position:absolute;left:24px;top:36px;width:170px;display:flex;align-items:center;gap:10px}
  .brand-mark{flex:none;width:22px;height:22px;background:var(--orange)}
  .brand-name{font-family:"Oswald",sans-serif;font-weight:600;font-size:27px;line-height:1.05;color:var(--green-deep);letter-spacing:1px}
  .title{position:absolute;left:346px;top:24px;width:384px;text-align:right;font-family:"Oswald",sans-serif;font-weight:600;font-size:37px;line-height:1.1;color:var(--white);letter-spacing:.5px}
  .subtitle{position:absolute;left:346px;top:78px;width:384px;text-align:right;font-size:21px;font-weight:500;color:var(--white);letter-spacing:.4px}
  .body{position:absolute;left:0;top:134px;width:748px;height:876px;background:linear-gradient(180deg,var(--sky-top) 0%,var(--sky-mid) 45%,var(--sky-low) 75%,#a9c98a 80%,var(--ground) 81%)}
  .body>svg.backdrop{position:absolute;inset:0}
  .card{position:absolute;border-radius:16px;overflow:hidden;background:var(--card);box-shadow:0 3px 8px rgba(0,0,0,.18)}
  .card-head{color:var(--white);font-weight:700;text-align:center;letter-spacing:.5px}
  .features{left:24px;top:42px;width:452px;height:318px}
  .features .card-head{background:var(--green);height:54px;line-height:56px;font-size:27px}
  .features ul{list-style:none;padding:14px 20px 0 30px}
  .features li{position:relative;font-size:15.4px;line-height:19.4px}
  .features li::before{content:"";position:absolute;left:-11px;top:7px;width:5px;height:5px;border-radius:50%;background:var(--orange)}
  .options{left:24px;top:390px;width:282px;height:270px}
  .options .card-head{background:var(--orange);height:46px;line-height:48px;font-size:22px}
  .options ul{list-style:none;padding:8px 10px 0 38px}
  .options li{position:relative;font-size:15px;line-height:20px;margin-bottom:2px}
  .options li svg{position:absolute;left:-30px;top:1px}
  .price-chip{display:inline-block;background:var(--green);color:var(--white);font-weight:500;padding:0 6px;line-height:19px}
  .note{font-style:italic}
  .thumb{position:absolute;width:142px;height:120px;border-radius:16px;border:4px solid var(--white);box-shadow:0 3px 8px rgba(0,0,0,.3);background:linear-gradient(180deg,#9cc0e4 0%,#dfe8f0 45%,#f4f4f2 46%,#e9e9e7 80%,#7d7f82 100%)}
  .thumb-1{left:566px;top:21px}
  .thumb-2{left:488px;top:154px}
  .thumb-3{left:404px;top:286px}
  .price{position:absolute;left:569px;top:322px;width:166px;height:166px;border-radius:50%;background:var(--orange);border:5px solid var(--white);color:var(--white);display:flex;flex-direction:column;align-items:center;justify-content:center;text-align:center}
  .price-label{font-size:17px;font-weight:500;line-height:1.2}
  .price-value{font-size:33px;font-weight:900;line-height:1.1}
  .hero{position:absolute;left:314px;top:419px;width:434px;height:457px;background:linear-gradient(160deg,#f7f7f5 0%,#e4e4e2 55%,#8e9194 100%);clip-path:polygon(8% 18%,100% 4%,100% 100%,4% 100%,0% 30%)}
  .use-title{position:absolute;left:26px;top:705px;font-size:27px;font-weight:700;color:var(--white)}
  .use-icons{position:absolute;left:26px;top:750px}
  .use-list{position:absolute;left:20px;top:805px;width:470px;font-size:11.6px;line-height:14.6px;color:var(--ink)}
  .footer{position:absolute;left:0;top:1010px;width:748px;height:48px}
  .footer svg{position:absolute;inset:0}
  .phone{position:absolute;left:118px;top:5px;font-size:31px;font-weight:700;color:var(--white);letter-spacing:.5px}
  .web{position:absolute;right:28px;top:10px;font-size:22px;font-weight:700;color:var(--orange)}
</style>
</head>
<body>
<div class="flyer">
  <header class="header">
    <svg width="748" height="134" viewBox="0 0 748 134">
      <polygon points="200,0 214,0 302,134 288,134" fill="var(--green)"/>
      <polygon points="222,0 234,0 322,134 310,134" fill="var(--orange)"/>
      <polygon points="244,0 748,0 748,134 334,134" fill="var(--orange)"/>
    </svg>
    <div class="brand"><span class="brand-mark"></span><span class="brand-name">BRIGHT CABIN<br>WORKS</span></div>
    <h1 class="title">THE MEADOW BARN MINI</h1>
    <p class="subtitle">Luxury, Mobile Vending House</p>
  </header>

  <section class="body">
    <svg class="backdrop" width="748" height="876" viewBox="0 0 748 876">
      <polygon points="367,192 748,12 748,876 314,876 314,623" fill="var(--green)"/>
      <polygon points="690,360 700,290 708,362" fill="var(--orange)"/>
      <polygon points="712,372 746,318 724,378" fill="var(--orange)"/>
      <rect x="0" y="690" width="748" height="186" fill="var(--ground)"/>
    </svg>

    <div class="thumb thumb-1" role="img" aria-label="Photo of the white vending house parked, front three-quarter view"></div>
    <div class="thumb thumb-2" role="img" aria-label="Photo of the vending house side with dormer windows"></div>

    <div class="hero" role="img" aria-label="Photo of the white board-and-batten vending house on a tandem-axle trailer with an open serving window"></div>

    <div class="card features">
      <h2 class="card-head">BASE UNIT FEATURES</h2>
      <ul>
        <li>Trailer features tandem wheels w/ brakes</li>
        <li>Steel frame construction for fire retardation<br>safety and weight reduction.</li>
        <li>100% off grid with solar and lithium<br>battery system allowing the trailer<br>to be used in places not accessible<br>by traditional trailers.</li>
        <li>80 gallon water supply tank</li>
        <li>100 gallon waste water tank</li>
        <li>Cupboards, cabinets &amp;<br>four stainless steel sinks.</li>
        <li>60” Gas shock serving window</li>
      </ul>
    </div>

    <div class="thumb thumb-3" role="img" aria-label="Photo of the vending house on its tandem trailer, rear side"></div>

    <div class="card options">
      <h2 class="card-head">AVAILABLE OPTIONS</h2>
      <ul>
        <li><svg width="18" height="18" viewBox="0 0 18 18"><circle cx="9" cy="9" r="9" fill="var(--orange)"/><path d="M4.5 9.2l3 3 6-6" stroke="#fff" stroke-width="2.2" fill="none"/></svg>HVAC - Aero Mini Split - <span class="price-chip">$1,800</span></li>
        <li><svg width="18" height="18" viewBox="0 0 18 18"><circle cx="9" cy="9" r="9" fill="var(--orange)"/><path d="M4.5 9.2l3 3 6-6" stroke="#fff" stroke-width="2.2" fill="none"/></svg>Cooler / Glass front<br>Commercial refrigerator - <span class="price-chip">$1,600</span></li>
        <li><svg width="18" height="18" viewBox="0 0 18 18"><circle cx="9" cy="9" r="9" fill="var(--orange)"/><path d="M4.5 9.2l3 3 6-6" stroke="#fff" stroke-width="2.2" fill="none"/></svg>Upper loft storage area - <span class="price-chip">$1,200</span></li>
        <li><svg width="18" height="18" viewBox="0 0 18 18"><circle cx="9" cy="9" r="9" fill="var(--orange)"/><path d="M4.5 9.2l3 3 6-6" stroke="#fff" stroke-width="2.2" fill="none"/></svg>Signage and graphics -<br>&nbsp;<span class="price-chip">$2,000 - $5,000</span><br><span class="note">(Depend on complexity)</span></li>
        <li><svg width="18" height="18" viewBox="0 0 18 18"><circle cx="9" cy="9" r="9" fill="var(--orange)"/><path d="M4.5 9.2l3 3 6-6" stroke="#fff" stroke-width="2.2" fill="none"/></svg>Ice machine - <span class="price-chip">$1,100</span></li>
        <li><svg width="18" height="18" viewBox="0 0 18 18"><circle cx="9" cy="9" r="9" fill="var(--orange)"/><path d="M4.5 9.2l3 3 6-6" stroke="#fff" stroke-width="2.2" fill="none"/></svg>Other custom items available<br>on request.</li>
      </ul>
    </div>

    <div class="price">
      <div class="price-label">BASE PRICE</div>
      <div class="price-value">$45,000</div>
    </div>

    <h3 class="use-title">Use Cases:</h3>
    <svg class="use-icons" width="230" height="50" viewBox="0 0 230 50" role="img" aria-label="Icons for food, retail, corporate and fundraisers">
      <circle cx="24" cy="24" r="23" fill="var(--orange)" stroke="#fff" stroke-width="2"/>
      <path d="M14 34l20-20M34 34L14 14" stroke="#fff" stroke-width="3" stroke-linecap="round"/>
      <circle cx="82" cy="24" r="23" fill="var(--green)" stroke="#fff" stroke-width="2"/>
      <path d="M72 20h20l-2 16H74z" fill="none" stroke="#fff" stroke-width="2.4"/>
      <path d="M77 20v-3a5 5 0 0 1 10 0v3" fill="none" stroke="#fff" stroke-width="2.4"/>
      <circle cx="140" cy="24" r="23" fill="var(--orange)" stroke="#fff" stroke-width="2"/>
      <circle cx="140" cy="19" r="7" fill="none" stroke="#fff" stroke-width="2.4"/>
      <path d="M127 32h26" stroke="#fff" stroke-width="3" stroke-linecap="round"/>
      <circle cx="198" cy="24" r="23" fill="var(--green)" stroke="#fff" stroke-width="2"/>
      <rect x="188" y="14" width="9" height="22" fill="none" stroke="#fff" stroke-width="2.2"/>
      <rect x="199" y="20" width="10" height="16" fill="none" stroke="#fff" stroke-width="2.2"/>
    </svg>
    <p class="use-list">
      <b>FOOD:</b> Lemonade, Coffee, pizza, cookies, doughnuts, barbecue and more!<br>
      <b>RETAIL:</b> Clothing, watches, jewelry, flowers and more!<br>
      <b>CORPORATE:</b> Product info, demonstration, information, brand awareness.<br>
      <b>FUNDRAISERS:</b> Girls/boy sports, non profits, etc.
    </p>
  </section>

  <footer class="footer">
    <svg width="748" height="48" viewBox="0 0 748 48">
      <rect x="0" y="0" width="56" height="48" fill="var(--orange)"/>
      <polygon points="56,0 330,0 356,48 56,48" fill="var(--green)"/>
      <path d="M20 14c0 9 6 16 15 18l3-4-4-3-2 2c-3-1-6-4-7-7l2-2-3-4z" fill="#fff"/>
    </svg>
    <div class="phone">555 210 487</div>
    <div class="web">www.brightcabinworks.com</div>
  </footer>
</div>
</body>
</html>
```